MORVEK IT Limited Buisness card logo

I am setting up a IT Consultancy company and want a logo that is related to the IT industry, but also i am thinking that the A in MOR and the A in VEK are linked together maybe horizontally and vertically, also thought about the A being @ as it symbolises IT services. This logo will be used on paperwork, business cards and website.

Industry/Entity Type

Business

Contact Information for Business Card

Gareth Wilmslow
MORVEK IT Limited
IT Consultant
Mobile: 07912563084
Email: garethwk@fernmail.co.uk

Requirements
Must have
• IT Theme

```html
<!DOCTYPE html>
<html lang="en">
<head>
<meta charset="utf-8">
<title>MORVEK IT Limited – Business Card</title>
<link rel="stylesheet" href="https://fonts.googleapis.com/css2?family=Lato:wght@300;400;700;900&display=swap">
<style>
  :root {
    --card-bg: #ffffff;
    --frame: #1a1a1a;
    --brand-blue: #3366ff;
    --brand-violet: #7448ff;
    --ink: #1c1c1c;
  }
  html, body {
    margin: 0;
    padding: 0;
    width: 1200px;
    height: 791px;
    overflow: hidden;
    background: var(--card-bg);
  }
  .card {
    position: relative;
    width: 1200px;
    height: 791px;
    background: var(--card-bg);
    font-family: "Lato", sans-serif;
  }
  .card__frame {
    position: absolute;
    left: 23px;
    top: 25px;
    width: 1152px;
    height: 739px;
    border: 2px solid var(--frame);
    box-sizing: border-box;
  }
  .brand {
    position: absolute;
    left: 84px;
    top: 165px;
    width: 1040px;
    height: 170px;
    display: flex;
    align-items: center;
    justify-content: space-between;
  }
  .brand__name {
    margin: 0;
    font-size: 162px;
    font-weight: 400;
    line-height: 1;
    letter-spacing: 9px;
    color: var(--brand-blue);
    white-space: nowrap;
  }
  .brand__mark {
    flex: none;
    width: 62px;
    height: 62px;
    margin-top: 8px;
    background: var(--brand-blue);
  }
  .contact {
    position: absolute;
    right: 75px;
    top: 484px;
    text-align: right;
    color: var(--ink);
    font-weight: 300;
    font-size: 35px;
    line-height: 53px;
    white-space: nowrap;
  }
  .contact p { margin: 0; }
  .contact__name {
    font-weight: 900;
    font-size: 37px;
    color: var(--brand-blue);
  }
  .contact__label {
    font-weight: 900;
    color: var(--brand-violet);
  }
  .contact__rule {
    position: absolute;
    left: 1140px;
    top: 497px;
    width: 10px;
    height: 267px;
    background: var(--brand-violet);
  }
</style>
</head>
<body>
  <main class="card">
    <div class="card__frame"></div>

    <div class="brand">
      <h1 class="brand__name">MORVEK IT</h1>
      <span class="brand__mark" aria-hidden="true"></span>
    </div>

    <section class="contact">
      <p class="contact__name">Gareth Wilmslow</p>
      <p>MORVEK IT Limited</p>
      <p>IT Consultant</p>
      <p><span class="contact__label">Mobile:</span> 07912 563084</p>
      <p><span class="contact__label">Email:</span> garethwk@fernmail.co.uk</p>
    </section>
    <div class="contact__rule"></div>
  </main>
</body>
</html>
```